Name for Roofing Company

We are a company that specialises in supply and installation of metal roofing to Commercial and Domestic buildings in Perth Western Australia. We are looking for someone to come up with a name that is catch innovative and marketable.

```html
<!DOCTYPE html>
<html lang="en">
<head>
<meta charset="utf-8">
<title>Ridge Iron — Name Proposal</title>
<link rel="stylesheet" href="https://fonts.googleapis.com/css2?family=Carlito&display=swap">
<style>
  :root {
    --accent-red: #aa0000;
    --title-ink: #2f2f2f;
    --paper-top: #fdfdfd;
    --paper-mid: #eeeeee;
    --paper-bottom: #dedede;
  }
  html, body {
    margin: 0;
    padding: 0;
    width: 1200px;
    height: 1200px;
    overflow: hidden;
  }
  .slide {
    position: relative;
    width: 1200px;
    height: 1200px;
    background: linear-gradient(180deg, var(--paper-top) 0%, var(--paper-mid) 45%, var(--paper-bottom) 100%);
    overflow: hidden;
  }
  .accent-block {
    position: absolute;
    left: 102px;
    top: 0;
    width: 990px;
    height: 532px;
    background: var(--accent-red);
  }
  .brand-title {
    position: absolute;
    left: 110px;
    top: 620px;
    margin: 0;
    font-family: "Carlito", "Calibri", sans-serif;
    font-weight: 400;
    font-size: 168px;
    line-height: 1;
    letter-spacing: -1px;
    color: var(--title-ink);
  }
  .footer-rule {
    position: absolute;
    left: 102px;
    top: 1079px;
    width: 990px;
    height: 3px;
    background: var(--accent-red);
  }
</style>
</head>
<body>
  <main class="slide">
    <div class="accent-block"></div>
    <h1 class="brand-title">Ridge Iron</h1>
    <div class="footer-rule"></div>
  </main>
</body>
</html>
```